都内でエステサロンを運営されている
美容家さんの電子書籍を出版しますので、
表紙デザイン作成をお願いいたします。

ーーーーーーーーーーー
■本のタイトル
月灯集

【サブタイトル】
朝の散歩で心を整える本

<著者>沙耶(さや)

ーーーーーーーーーー

納品は、2,560 x 1,600 ピクセルのJPEGと
元データをお願い致したく。

著者プロフィール
美容家、エステティシャン

サロンのイメージカラーはピンク、白ですが
表紙デザインに色のこだわりはありません。

ーーーー

■デザイン要望

優しさ,明るさ、清潔感と品格、プロフェッショナル感があるものをお願いします。

【コンセプト】
美容ジプシー、悩める女性たちに(男性も歓迎)贈りたい
優しく楽しい小さなご褒美タイムとその作法(洗顔やお肌のお手入れに関するメソッド)を提供する

肌質はみんなそれぞれちがいますが、本当に幸せな自分磨きは毎日のスキンケア一択。その極意を惜しみなく提供。

添付に表紙イメージの参考を挙げましたが
デザイナー様のセンスにお任せします。

ーーーーーーーーーー

※その他イラストや写真等素材を使用される場合には、商用利用可の素材をお願いします。
(Pavrelにて販売予定のため)

デザインを考えるのに必要な情報などありましたら、お答えしますので、ご遠慮なくお問い合わせ下さい。

納期は予告なく短縮する場合がございます。
よろしくお願い申し上げます。

著者様のご希望優先で決定させていただきました。

美容の道を極めた想いと、透明感、躍動感、生き生きとした理想の美人像を彷彿とさせる素敵な表紙ということで、選定させていただきます。

この度は、当コンペにご提案を頂き誠にありがとうございます。
リピートのデザイナー様もいらして、どれも素晴らしく貴重なお時間と労力を割いてくださって
本当にありがとうございました。心より感謝申し上げます。

今回選定できなかった方々の作品も大切に拝見し、個別に依頼できそうな案件などありましたらご紹介させていただきます。みなさまのご活躍祈念しております。

これからも大切に作品を制作してまいります。
どうぞまたコンペ開催の際にはご縁をいただけましたら幸いです。

本当にどうもありがとうございました。

```html
<!DOCTYPE html>
<html lang="ja">
<head>
<meta charset="UTF-8">
<title>月灯集 — 沙耶</title>
<link rel="stylesheet" href="https://fonts.googleapis.com/css2?family=Noto+Serif+JP:wght@400;600;700;900&family=Zen+Maru+Gothic:wght@500;700&display=swap">
<style>
  :root {
    --bg-light: #e4e1de;
    --bg-mid: #b7b3b0;
    --bg-shadow: #a9a4a0;
    --bg-warm: #c4ab9c;
    --bg-hair: #8d8581;
    --title-white: #ffffff;
    --ink: #1b1b1b;
    --badge-yellow: #f7dc2a;
    --badge-ink: #222222;
  }
  * { margin: 0; padding: 0; box-sizing: border-box; }
  html, body {
    width: 750px; height: 1200px; overflow: hidden;
    background: var(--bg-light);
  }
  .cover {
    position: relative;
    width: 750px; height: 1200px;
    overflow: hidden;
    font-family: "Noto Serif JP", serif;
  }
  .cover-photo {
    position: absolute; inset: 0;
    background:
      radial-gradient(ellipse 30% 22% at 38% 38%, var(--bg-hair) 0%, rgba(141,133,129,0) 75%),
      radial-gradient(ellipse 45% 35% at 55% 50%, var(--bg-warm) 0%, rgba(196,171,156,0) 75%),
      radial-gradient(ellipse 35% 45% at 85% 80%, #e6ddd6 0%, rgba(230,221,214,0) 70%),
      linear-gradient(100deg, var(--bg-shadow) 0%, var(--bg-mid) 40%, var(--bg-light) 100%);
  }
  .vertical { writing-mode: vertical-rl; text-orientation: upright; }
  .book-title {
    position: absolute;
    left: 10px; top: 20px;
    font-size: 330px;
    line-height: 1;
    font-weight: 400;
    color: var(--title-white);
    letter-spacing: 0.06em;
    text-shadow: 0 2px 18px rgba(0,0,0,0.22);
  }
  .subtitle {
    position: absolute;
    right: 22px; top: 22px;
    font-size: 94px;
    line-height: 1;
    font-weight: 700;
    color: var(--ink);
    letter-spacing: 0.09em;
  }
  .author {
    position: absolute;
    left: 365px; top: 36px;
    display: flex;
    flex-direction: row-reverse;
    align-items: flex-start;
    gap: 8px;
    color: var(--ink);
  }
  .author-profile {
    font-size: 22px;
    line-height: 1.35;
    font-weight: 600;
    letter-spacing: 0.08em;
  }
  .author-name-wrap {
    display: flex;
    flex-direction: row-reverse;
    align-items: flex-start;
    margin-top: 110px;
    gap: 4px;
  }
  .author-name {
    font-size: 72px;
    line-height: 1;
    font-weight: 700;
    letter-spacing: 0.12em;
  }
  .author-reading {
    font-size: 22px;
    line-height: 1;
    font-weight: 600;
    letter-spacing: 0.3em;
    margin-top: 70px;
  }
  .bonus-badge {
    position: absolute;
    left: 462px; top: 982px;
    width: 160px; height: 160px;
    border-radius: 50%;
    background: var(--badge-yellow);
    color: var(--badge-ink);
    display: flex;
    flex-direction: column;
    align-items: center;
    justify-content: center;
    text-align: center;
    font-family: "Zen Maru Gothic", sans-serif;
    font-weight: 700;
    line-height: 1.12;
  }
  .bonus-label { font-size: 16px; margin-bottom: 4px; letter-spacing: 0.03em; }
  .bonus-small { font-size: 13px; }
  .bonus-big { font-size: 24px; }
  .bonus-mid { font-size: 18px; }
</style>
</head>
<body>
  <main class="cover">
    <div class="cover-photo" role="img" aria-label="明るいグレーの背景で、両腕を上げて笑顔を見せる女性の写真"></div>

    <h1 class="book-title vertical">月灯集</h1>

    <p class="subtitle vertical">朝の散歩で心を整える本</p>

    <div class="author">
      <p class="author-profile vertical">美容家<br>エステティシャン</p>
      <div class="author-name-wrap">
        <p class="author-name vertical">沙耶</p>
        <p class="author-reading vertical">さや</p>
      </div>
    </div>

    <aside class="bonus-badge">
      <span class="bonus-label">★無料特典★</span>
      <span class="bonus-small">ツヤツヤ</span>
      <span class="bonus-big">たまご肌</span>
      <span class="bonus-small">をつくる</span>
      <span class="bonus-mid">洗顔ステップ</span>
      <span class="bonus-mid">動画</span>
    </aside>
  </main>
</body>
</html>
```